Stanbrook Fire Services Pty Ltd

We need business cards for a company based in Perth, we install, service and maintain fire equipment.
On the front we want a great design with our logo and a small spot for our full company name, general company email address and office number. On the back we need space for our name, title, mobile number and email address on the back.

Target Market(s)

Facility managers and commercial/industrial building owners/occupiers.

Contact Information for Business Card

Font styles to use
Sans Serif

Requirements
Must have
• Please only submit 5 of your best samples.
Darker tones are preferred.
Nice to have
• We want to use, black, red and grey. Keep it modern and clean.
I've attached the company logo and a sample of a boarder we use on our emergency plans.
Should not have
• No preference. Let the designer choose.

```html
<!DOCTYPE html>
<html lang="en">
<head>
<meta charset="utf-8">
<title>Stanbrook Fire Services – Business Card</title>
<link href="https://fonts.googleapis.com/css2?family=Roboto:wght@300;400;500;700&display=swap" rel="stylesheet">
<style>
  :root {
    --bg: #2b2b2d;
    --card: #1c1d1f;
    --card-back: #1f2022;
    --pattern: #28292b;
    --red: #e3171f;
    --text: #e6e6e6;
    --rule: #9a9a9a;
  }
  * { margin: 0; padding: 0; box-sizing: border-box; }
  html, body {
    width: 1200px; height: 1108px; overflow: hidden;
    background: var(--bg);
    font-family: "Roboto", Arial, sans-serif;
  }
  .stage { position: relative; width: 1200px; height: 1108px; }
  .card {
    position: absolute; top: 214px;
    width: 400px; height: 680px;
    border-radius: 26px;
    overflow: hidden;
  }
  .card--front { left: 170px; background: var(--card); }
  .card--back { left: 630px; background: var(--card-back); }

  .front__brand {
    position: absolute; top: 120px; left: 0; right: 0;
    text-align: center;
    color: var(--red);
    font-weight: 700; font-size: 54px; letter-spacing: 1px;
  }
  .front__details {
    position: absolute; top: 360px; left: 60px; right: 60px;
    text-align: center; color: var(--text);
  }
  .person__name { color: var(--red); font-size: 25px; font-weight: 500; }
  .person__title { font-size: 19px; font-weight: 400; margin-top: 2px; }
  .divider {
    display: flex; align-items: center; gap: 6px;
    margin: 16px 0 12px;
  }
  .divider::before, .divider::after {
    content: ""; flex: 1; height: 1px; background: var(--rule);
  }
  .divider__icons { display: flex; gap: 4px; }
  .contact-list { list-style: none; font-size: 18px; font-weight: 300; line-height: 1.45; }
  .contact-list .accent { color: var(--red); }
  .rule { height: 1px; background: var(--rule); margin: 12px 0; }
  .address { font-size: 18px; font-weight: 300; line-height: 1.3; }

  .back__pattern {
    position: absolute; inset: 0;
    background: linear-gradient(160deg, var(--pattern), var(--card-back));
  }
  .back__brand {
    position: absolute; right: 40px; bottom: 110px;
    color: var(--red); font-weight: 700; font-size: 26px; letter-spacing: 1px;
  }
</style>
</head>
<body>
<main class="stage">
  <section class="card card--front" aria-label="Card front">
    <div class="front__brand">STANBROOK</div>
    <div class="front__details">
      <p class="person__name">Daniel Hayes</p>
      <p class="person__title">Manager</p>
      <div class="divider">
        <span class="divider__icons">
          <svg width="22" height="22" viewBox="0 0 22 22" aria-label="Phone">
            <circle cx="11" cy="11" r="11" fill="var(--red)"/>
            <path d="M7 6.5c0.8-0.6 1.6 0 2 0.8l0.6 1.3c0.2 0.5 0 1-0.4 1.3l-0.5 0.4c0.5 1.2 1.5 2.2 2.7 2.7l0.4-0.5c0.3-0.4 0.8-0.6 1.3-0.4l1.3 0.6c0.8 0.4 1.4 1.2 0.8 2-1 1.3-2.6 1.4-4.3 0.4-1.8-1-3.3-2.5-4.3-4.3-1-1.7-0.9-3.3 0.4-4.3z" fill="#fff"/>
          </svg>
          <svg width="22" height="22" viewBox="0 0 22 22" aria-label="Email">
            <circle cx="11" cy="11" r="11" fill="var(--red)"/>
            <rect x="5.5" y="7.5" width="11" height="7.5" rx="1" fill="#fff"/>
            <path d="M5.8 8l5.2 4 5.2-4" stroke="var(--red)" stroke-width="1.2" fill="none"/>
          </svg>
          <svg width="22" height="22" viewBox="0 0 22 22" aria-label="Website">
            <circle cx="11" cy="11" r="11" fill="var(--red)"/>
            <circle cx="11" cy="11" r="5.5" stroke="#fff" stroke-width="1.3" fill="none"/>
            <ellipse cx="11" cy="11" rx="2.3" ry="5.5" stroke="#fff" stroke-width="1.1" fill="none"/>
            <line x1="5.5" y1="11" x2="16.5" y2="11" stroke="#fff" stroke-width="1.1"/>
          </svg>
        </span>
      </div>
      <ul class="contact-list">
        <li>08 9412 3570</li>
        <li>office@stanbrookfire.com</li>
        <li>www.<span class="accent">yourwebsite</span>.com</li>
      </ul>
      <div class="rule"></div>
      <p class="address">Your address, city<br>state, ZIP 0000</p>
    </div>
  </section>

  <section class="card card--back" aria-label="Card back">
    <div class="back__pattern" role="img" aria-label="Faint repeating tone-on-tone company name pattern"></div>
    <div class="back__brand">STANBROOK</div>
  </section>
</main>
</body>
</html>
```